A brand new wordpress website for my business which will replace my current site www.harbornetcall.com.au, As i rank quite well in google will it be ok to keep my current URL's. I sell the following service and products

1. Voip Provider (Main service) we sell directly the the end user but also we would like to get resellers and agents to sell our services. agents selling our brand resellers sell our services branded as theirs
2. Hosted Pbx (main service) home page must push this service explaining the benifits and features that come with a hosted pbx, we also have business plans based on number of extensions (phones) the customer requires
3. Tornax IP Pbx (product) only selling IP Pbx and selected software
4. Velbox IP Pbx (product)
5. Quorvin IP Phones (this is the main VoIP phone we sell)
6. lumora phones (to be on a landing page only not apart of the main site)
7. selected headsets from Dravensonic (products)
8. Meridal Conference phone (VoIP model only)
9. we can supply fax to email service

we would like a support page with user guides (step by step instructions on our products and services and FAQ's about all products and services

we have a carrier grade softswitch (telco billing system) z7ledger http://www.pinwheelledger.org this system has a ticketing system, customer and agent login I would like a URL link from our website so customers can login to this system. also it is possible to skin z7ledger to look like our website

VoIP business plans

$0 per month
call rate .12c land line calls
.24c per minute mobile calls

$25 per month
250 Free local land line calls
call rate is .10c land line calls .22c per minute mobile calls

$50 per month
500 Free local land line calls
call rate .09 land line calls .20c per minute mobile calls

$100 per month
1000 free local land line calls
call rate .08c land line calls .18c per minute mobile calls

all mobile calls are billed per second no flag fall

also require a link to international call rates

We can port your existing telephone number from any carrier or supply new Australian telephone numbers

02, 03, 07, 08, 131, 1300, 1800

Designs i like www.tralcom.com.au and www.orbitelphone.com

I would like the website to be white and bright

Reason: Please use images of the products I sell only

Target Market(s)

business customers only

Industry/Entity Type

Requirements
Must have
• all pages must have its own banner to reflect the product or service we are selling. the home page can automatically change to show all pages with a link straight to the page in question

for example if on the home page the banner for quorvin phone is displaying if someone click on the banner they will be redirected to the quorvin page

Must Be SEO friendly
Nice to have
• shopping cart via paypal for all products but before customer checks out i would like to offer two options

1. Pre configure the item and ship to your address for existing customers
2. would you like a harbor net call technician to attend your office and install the item in person (costs involved $60 call out fee $120 per hours every item sold charge .50 hour and only the one call out fee)

new and existing customers can book service work via the website
1. describe the work required (maybe we need to give a few option)
2. company details
3. pre payment (checkout via paypal) can we put the paypal fees back on to the customer?

```html
<!DOCTYPE html>
<html lang="en">
<head>
<meta charset="utf-8">
<title>Harbor Net Call – Business VoIP</title>
<link href="https://fonts.googleapis.com/css2?family=Ubuntu:wght@400;500;700&display=swap" rel="stylesheet">
<style>
:root{
  --brand:#2d4f88;
  --brand-dark:#1f3c6e;
  --banner:#4469a8;
  --banner-light:#5a7fbd;
  --nav:#3a5f9e;
  --accent:#f2c500;
  --text:#444;
  --muted:#777;
  --card:#f1f1f1;
  --line:#d6d6d6;
  --footer:#2f2f2f;
  --footer-text:#d8d8d8;
  --white:#fff;
}
*{margin:0;padding:0;box-sizing:border-box}
html,body{width:720px;height:1200px;overflow:hidden;background:var(--white)}
body{font-family:'Ubuntu',sans-serif;color:var(--text)}
.page{position:relative;width:720px;height:1200px;overflow:hidden}
.abs{position:absolute}

/* header */
.phone-pill{left:486px;top:0;width:134px;height:28px;background:#eef0f3;border-radius:0 0 18px 18px;display:flex;align-items:center;gap:8px;padding-left:8px;font-weight:700;font-size:12px;color:var(--brand-dark)}
.phone-pill svg{width:14px;height:14px}
.logo{left:88px;top:32px;font-size:22px;font-weight:700;color:var(--brand);letter-spacing:.2px}
.logo-dot{display:inline-block;width:12px;height:12px;border-radius:50%;background:var(--brand);margin-right:6px;vertical-align:1px}
.search{left:473px;top:42px;width:134px;height:17px;border:1px solid #c9ced6;border-radius:2px;display:flex;font-size:7px;color:#999;background:#fff}
.search span{flex:1;display:flex;align-items:center;padding-left:8px;gap:5px}
.search button{width:25px;border:0;background:var(--brand);color:#fff;font:500 7px 'Ubuntu',sans-serif}
.top-links{right:112px;top:72px;font-size:7.5px;color:#333}
.top-links a{color:#333;text-decoration:none}

/* banner */
.banner{left:0;top:93px;width:720px;height:217px;background:linear-gradient(#4d72b0,#4266a5);overflow:hidden}
.cloud{position:absolute;background:var(--banner-light);border-radius:50%;opacity:.55}
.nav{left:86px;top:0;width:526px;height:29px;background:var(--nav);display:flex;align-items:center;font-size:9px;color:#fff}
.nav a{color:#fff;text-decoration:none;padding:0 5.5px}
.nav a.active{color:var(--accent);padding-left:16px;width:139px}
.banner-title{left:118px;top:73px;font-size:13px;font-weight:500;color:#fff}
.banner-copy{left:116px;top:97px;width:190px;font-size:6.5px;line-height:10.4px;color:#e6ecf6;text-align:justify}
.btn-more{left:117px;top:152px;width:42px;height:17px;border-radius:4px;background:#f3f3f3;font-size:7px;color:#333;display:flex;align-items:center;justify-content:center}
.product-visual{left:345px;top:52px;width:200px;height:140px;border-radius:40px 60px 50px 30px;background:radial-gradient(circle at 60% 50%,#3a3d44,#22252b 60%,rgba(34,37,43,0) 72%)}
.arrow{width:24px;height:24px;border-radius:50%;background:#e8e8e8;top:96px;display:flex;align-items:center;justify-content:center;box-shadow:0 1px 3px rgba(0,0,0,.35)}

/* plans */
.section-title{left:84px;top:325px;font-size:18px;font-weight:700;color:var(--brand)}
.plan-name{font-size:13px;color:var(--brand);top:370px}
.plan{top:390px;width:121px;height:170px;background:linear-gradient(#fafafa,#ececec);border:1px solid #e1e1e1;border-radius:4px;box-shadow:0 6px 6px -4px rgba(0,0,0,.35);text-align:center;font-size:7.5px;color:#666;line-height:14.5px}
.price{margin-top:7px;color:#555;font-size:10px;display:flex;justify-content:center;align-items:baseline;gap:3px}
.price b{font-size:24px;color:var(--brand);font-weight:500}
.plan p{position:absolute;left:6px;right:6px}
.plan .btn{position:absolute;left:30px;bottom:10px;width:61px;height:24px;background:linear-gradient(#3b5f9c,#264981);border-radius:2px;color:#fff;font-size:9.5px;line-height:24px}

/* services & products */
.sub-title{font-size:12px;font-weight:700;color:var(--brand)}
.sub-rule{height:1px;background:linear-gradient(90deg,#c9c9c9,rgba(255,255,255,0))}
.tile{width:101px}
.tile-img{position:relative;height:67px;border:2px solid #d3d3d3;border-radius:3px;overflow:hidden}
.tile-img .cap{position:absolute;left:0;right:0;bottom:0;height:15px;background:rgba(30,30,30,.7);color:#fff;font-size:9.5px;padding-left:4px;line-height:15px;white-space:nowrap}
.tile p{font-size:6px;line-height:8px;color:#666;margin-top:3px;padding:0 1px}
.tile .more{font-size:7px;color:var(--brand);font-weight:500;margin-top:4px;display:flex;align-items:center;gap:5px}
.tile .more i{width:7px;height:7px;border-radius:50%;background:#8fb0d8;display:inline-block}

/* testimonials */
.testimonial-band{left:0;top:943px;width:720px;height:122px;background:#f3f3f3}
.desk-phone{left:110px;top:965px;width:100px;height:90px;border-radius:14px;background:radial-gradient(circle at 50% 55%,#3b3e45,#1e2025 62%,rgba(243,243,243,0) 74%)}
.quote{left:255px;top:950px;width:358px;height:102px;background:#fff;border:1px solid #e2e2e2;border-radius:5px}
.quote-tail{left:224px;top:984px}
.quote h3{position:absolute;left:18px;top:10px;font-size:11px;font-weight:500;color:var(--brand-dark)}
.quote .rule{position:absolute;left:18px;top:26px;width:130px;height:1px;background:#ccc}
.quote p{position:absolute;left:29px;top:35px;width:309px;font-size:6.5px;line-height:10.6px;color:#555;text-align:justify}
.quote cite{position:absolute;right:35px;top:78px;font-size:7px;color:var(--brand);font-style:normal}

/* footer */
.footer{left:0;top:1065px;width:720px;height:135px;background:var(--footer)}
.foot-col{top:17px;color:var(--footer-text)}
.foot-col h4{font-size:8.5px;font-weight:400;color:#fff;margin-bottom:7px}
.foot-col li{list-style:none;font-size:7px;line-height:15.2px;padding-left:10px;position:relative}
.foot-col li::before{content:'›';position:absolute;left:0;color:#aaa}
.social{left:480px;top:25px;display:flex;gap:8px}
.social span{width:16px;height:16px;border-radius:2px}
.copyright{right:107px;top:58px;font-size:7px;line-height:11px;color:var(--footer-text);text-align:right}
</style>
</head>
<body>
<div class="page">

  <header>
    <div class="abs phone-pill">
      <svg viewBox="0 0 16 16"><circle cx="8" cy="8" r="7" fill="none" stroke="#555" stroke-width="1.2"/><path d="M6 4.5c-.8.4-1.2 1.4-.7 2.8.6 1.7 1.8 3.3 3.2 4 .9.4 1.6.2 2-.3l-1-1.4-1 .4c-.8-.5-1.4-1.4-1.7-2.4l.8-.7z" fill="#555"/></svg>
      284 611 903
    </div>
    <div class="abs logo"><span class="logo-dot"></span>harbor net call</div>
    <div class="abs search">
      <span><svg width="8" height="8" viewBox="0 0 10 10"><circle cx="4" cy="4" r="3" fill="none" stroke="#888" stroke-width="1.2"/><path d="M6.3 6.3l3 3" stroke="#888" stroke-width="1.2"/></svg>Search</span>
      <button>GO</button>
    </div>
    <nav class="abs top-links"><a>Products</a> | <a>Support</a> | <a>Partners</a> | <a>About Us</a> | <a>Contact Us</a></nav>
  </header>

  <section class="abs banner">
    <div class="cloud" style="left:40px;top:40px;width:60px;height:45px"></div>
    <div class="cloud" style="left:62px;top:30px;width:66px;height:60px"></div>
    <div class="cloud" style="left:-40px;top:140px;width:260px;height:140px"></div>
    <div class="cloud" style="left:170px;top:160px;width:200px;height:110px"></div>
    <div class="cloud" style="left:340px;top:175px;width:240px;height:100px"></div>
    <div class="cloud" style="left:520px;top:150px;width:260px;height:130px"></div>
    <div class="cloud" style="left:600px;top:95px;width:160px;height:140px"></div>

    <nav class="abs nav">
      <a class="active">Products</a><a>Business VoIP Plans</a><a>Hosted PBX</a><a>Managed PBX</a><a>Fax to Email</a><a>Hardware</a><a>Add-on Services</a>
    </nav>
    <h1 class="abs banner-title">DRAVENSONIC HEADSETS</h1>
    <p class="abs banner-copy">Sed ut perspiciatis unde omnis iste natus error sit voluptatem accusantium doloremque laudantium, totam rem aperiam, eaque ipsa quae ab illo inventore veritatis et quasi architecto beatae vitae dicta sunt explicabo.</p>
    <div class="abs btn-more">More</div>
    <div class="abs product-visual" role="img" aria-label="Black wireless Bluetooth headset"></div>
    <div class="abs arrow" style="left:30px"><svg width="10" height="10" viewBox="0 0 10 10"><path d="M6.5 1.5L3 5l3.5 3.5" fill="none" stroke="#333" stroke-width="1.8"/></svg></div>
    <div class="abs arrow" style="left:661px"><svg width="10" height="10" viewBox="0 0 10 10"><path d="M3.5 1.5L7 5 3.5 8.5" fill="none" stroke="#333" stroke-width="1.8"/></svg></div>
  </section>

  <main>
    <h2 class="abs section-title">VoIP Business Plans</h2>

    <div class="abs plan-name" style="left:90px">Business Starter</div>
    <div class="abs plan" style="left:89px">
      <div class="price">$ <b>0</b> per month</div>
      <p style="top:60px">call rate .12c land line calls</p>
      <p style="top:99px">.24c per minute mobile calls</p>
      <div class="btn">MORE</div>
    </div>

    <div class="abs plan-name" style="left:223px">Small Business Saver</div>
    <div class="abs plan" style="left:222px">
      <div class="price">$ <b>25</b> per month</div>
      <p style="top:60px">250 Free local land line calls</p>
      <p style="top:93px;left:14px;right:14px;text-align:left">call rate is .10c land line calls .22c per minute mobile calls</p>
      <div class="btn">MORE</div>
    </div>

    <div class="abs plan-name" style="left:356px">Super Saver</div>
    <div class="abs plan" style="left:354px">
      <div class="price">$ <b>50</b> per month</div>
      <p style="top:60px">500 Free local land line calls</p>
      <p style="top:93px;left:14px;right:14px;text-align:left">call rate .09 land line calls .20c per minute mobile calls</p>
      <div class="btn">MORE</div>
    </div>

    <div class="abs plan-name" style="left:489px">Extreme Saver</div>
    <div class="abs plan" style="left:487px">
      <div class="price">$<b>100</b> per month</div>
      <p style="top:60px">1000 free local land line calls</p>
      <p style="top:93px;left:14px;right:14px;text-align:left">call rate .08c land line calls .18c per minute mobile calls</p>
      <div class="btn">MORE</div>
    </div>

    <h3 class="abs sub-title" style="left:90px;top:590px">OUR SERVICES</h3>
    <div class="abs sub-rule" style="left:90px;top:609px;width:280px"></div>

    <div class="abs tile" style="left:84px;top:630px">
      <div class="tile-img" role="img" aria-label="Office desk phone with handset" style="background:linear-gradient(135deg,#f4f4f4,#9aa1ab)"><div class="cap">VoIP Provider</div></div>
      <p>Sed ut perspiciatis unde omnis iste natus error sit voluptatem accusantium doloremque rem ,</p>
      <div class="more"><i></i>More</div>
    </div>
    <div class="abs tile" style="left:196px;top:630px">
      <div class="tile-img" role="img" aria-label="Telephone handset on a desk" style="background:linear-gradient(135deg,#e6e6e6,#8d8d8d)"><div class="cap">Hosted Pbx</div></div>
      <p>Sed ut perspiciatis unde omnis iste natus error sit voluptatem accusantium doloremque rem ,</p>
      <div class="more"><i></i>More</div>
    </div>
    <div class="abs tile" style="left:310px;top:630px">
      <div class="tile-img" role="img" aria-label="Rising green arrow over documents" style="background:linear-gradient(135deg,#e9ecef,#8fa89a)"><div class="cap">Ongoing Maintenance</div></div>
      <p>Sed ut perspiciatis unde omnis iste natus error sit voluptatem accusantium doloremque rem ,</p>
      <div class="more"><i></i>More</div>
    </div>
    <div class="abs tile" style="left:425px;top:630px">
      <div class="tile-img" role="img" aria-label="Financial figures on paper with a pen" style="background:linear-gradient(135deg,#f3f3f5,#b2b6c2)"><div class="cap">Office Audits</div></div>
      <p>Sed ut perspiciatis unde omnis iste natus error sit voluptatem accusantium doloremque rem ,</p>
      <div class="more"><i></i>More</div>
    </div>
    <div class="abs tile" style="left:539px;top:630px">
      <div class="tile-img" role="img" aria-label="Black IP desk phone keypad" style="background:linear-gradient(135deg,#d9d9d9,#4a4a4a)"><div class="cap">IP Pbx installations</div></div>
      <p>Sed ut perspiciatis unde omnis iste natus error sit voluptatem accusantium doloremque rem ,</p>
      <div class="more"><i></i>More</div>
    </div>

    <h3 class="abs sub-title" style="left:95px;top:771px">OUR PRODUCTS</h3>
    <div class="abs sub-rule" style="left:95px;top:790px;width:280px"></div>

    <div class="abs tile" style="left:89px;top:811px">
      <div class="tile-img" role="img" aria-label="Quorvin IP desk phone" style="background:linear-gradient(135deg,#c9ccd1,#2f3238)"><div class="cap">VoIP Provider</div></div>
      <p>Sed ut perspiciatis unde omnis iste natus error sit voluptatem accusantium doloremque rem ,</p>
      <div class="more"><i></i>More</div>
    </div>
    <div class="abs tile" style="left:202px;top:811px">
      <div class="tile-img" role="img" aria-label="Tornax PBX rack unit" style="background:linear-gradient(135deg,#9b9690,#3d3b38)"><div class="cap">Tornax PBX</div></div>
      <p>Sed ut perspiciatis unde omnis iste natus error sit voluptatem accusantium doloremque rem ,</p>
      <div class="more"><i></i>More</div>
    </div>
    <div class="abs tile" style="left:316px;top:811px">
      <div class="tile-img" role="img" aria-label="Velbox IP PBX appliance" style="background:linear-gradient(135deg,#e4e6ea,#3a3f48)"><div class="cap">Velbox</div></div>
      <p>Sed ut perspiciatis unde omnis iste natus error sit voluptatem accusantium doloremque rem ,</p>
      <div class="more"><i></i>More</div>
    </div>
    <div class="abs tile" style="left:431px;top:811px">
      <div class="tile-img" role="img" aria-label="Dravensonic headset with base unit" style="background:linear-gradient(135deg,#eeeeee,#3a3a3a)"><div class="cap">Dravensonic Headsets</div></div>
      <p>Sed ut perspiciatis unde omnis iste natus error sit voluptatem accusantium doloremque rem ,</p>
      <div class="more"><i></i>More</div>
    </div>
  </main>

  <section>
    <div class="abs testimonial-band"></div>
    <div class="abs desk-phone" role="img" aria-label="Black IP desk phone with colour screen"></div>
    <svg class="abs quote-tail" width="34" height="30" viewBox="0 0 34 30"><path d="M32 2 L2 26 L32 18" fill="#fff" stroke="#e2e2e2"/></svg>
    <div class="abs quote">
      <h3>Customer Testimonials</h3>
      <div class="rule"></div>
      <p>Sed ut perspiciatis unde omnis iste natus error sit voluptatem accusantium doloremque laudantium, totam rem aperiam, eaque ipsa quae ab illo inventore veritatis et quasi architecto beatae vitae dicta sunt explicabo. eaque ipsa quae ab illo inventore veritatis et quasi architecto beatae vitae dicta sunt explicabo.</p>
      <cite>-- Marcus , Sydney</cite>
    </div>
  </section>

  <footer class="abs footer">
    <div class="abs foot-col" style="left:82px">
      <h4>Products</h4>
      <ul><li>Sed ut perspiciatis unde</li><li>Omnis iste natus error sit</li><li>Voluptatem accusantium</li><li>Doloremque laudantium,</li><li>Totam rem aperiam, eaque</li><li>Voluptatem accusantium</li></ul>
    </div>
    <div class="abs foot-col" style="left:196px">
      <h4>Links</h4>
      <ul><li>Sed ut perspiciatis unde</li><li>Omnis iste natus error sit</li><li>Voluptatem accusantium</li><li>Doloremque laudantium,</li><li>Totam rem aperiam, eaque</li><li>Voluptatem accusantium</li></ul>
    </div>
    <div class="abs foot-col" style="left:316px">
      <h4>Links</h4>
      <ul><li>Sed ut perspiciatis unde</li><li>Omnis iste natus error sit</li><li>Voluptatem accusantium</li><li>Doloremque laudantium,</li><li>Totam rem aperiam, eaque</li><li>Voluptatem accusantium</li></ul>
    </div>
    <div class="abs social" aria-label="Social links">
      <span style="background:#3b5998"></span>
      <span style="background:#33aadd"></span>
      <span style="background:#ececec"></span>
      <span style="background:#f39a1e"></span>
      <span style="background:#cc2020"></span>
      <span style="background:#7fa6c9"></span>
    </div>
    <div class="abs copyright">© 2013 Harbornetcall, All Rights Reserved<br>x2</div>
  </footer>

</div>
</body>
</html>
```